Therapy Dog Organization Website

Looking for a website that is user friendly, welcoming, dog themed and has the following pages and links:
*Click here to join - links to a jot form
*Click here to donate - links to our paypal page
*Request a visit - links to a jot form
*Facebook Follow Link
*Instagram Follow Link
*Our team - images uploaded to showcase our dogs
*Donors and Referrals Page - Where I can update as donations and referrals come in.
*Online store. Currently this is in Jot Form but I would like a store front. I would not want this to be a link but rather a hidden page, something like www.hollowbirch.org/teamstore.

Please visit www.hollowbirch.org to see what we have right now designed simply in Canva. Dog photos can be provided to use in images.

Note: I have funds from a grant that I have to spend to add gratuity to the project winner.

```html
<!DOCTYPE html>
<html lang="en">
<head>
<meta charset="utf-8">
<title>Hollow Birch Therapy Dogs</title>
<link rel="stylesheet" href="https://fonts.googleapis.com/css2?family=Dela+Gothic+One&family=Outfit:wght@400;500;600&display=swap">
<style>
:root{
  --teal:#2ac8d0;
  --teal-dark:#1fb3bb;
  --ink:#111111;
  --pink:#f9e1e4;
  --mist:#e3e6e8;
  --white:#ffffff;
  --muted:#3a3a3a;
}
*{box-sizing:border-box;margin:0;padding:0}
html,body{width:1200px;height:4149px;overflow:hidden}
body{position:relative;background:var(--white);font-family:"Outfit",sans-serif;color:var(--ink)}
.abs{position:absolute}
.display{font-family:"Dela Gothic One",sans-serif;text-transform:uppercase;line-height:1.12;color:var(--ink);white-space:nowrap}
.btn{position:absolute;display:flex;align-items:center;justify-content:center;background:var(--teal);color:var(--ink);border-radius:40px;font-size:11px;font-weight:500;text-decoration:none}
.copy{font-size:9.5px;line-height:1.6;color:var(--muted)}
.photo{position:absolute}
.ring{border-radius:50%;border:4px solid var(--teal);overflow:hidden}
.spark{position:absolute;width:40px;height:34px}
.section-title{font-size:28px}

.hero-bg{left:-320px;top:0;width:1840px;height:710px;border-radius:0 0 50% 50%/0 0 230px 230px;background:linear-gradient(180deg,var(--mist) 0%,#f3e3e6 45%,var(--pink) 100%)}
.nav{left:93px;top:32px;width:1012px;height:84px;background:var(--white);border-radius:42px;box-shadow:0 4px 18px rgba(0,0,0,.06)}
.brand{display:flex;align-items:center;gap:10px;font-family:"Outfit",sans-serif;font-weight:600;font-size:26px;color:var(--ink);white-space:nowrap}
.brand-dot{width:26px;height:26px;border-radius:50%;background:var(--ink)}
.menu{right:14px;top:14px;width:58px;height:58px;border-radius:50%;background:var(--teal)}
.hero-photo{left:632px;top:116px;width:441px;height:472px;border-radius:0 0 220px 220px;background:linear-gradient(160deg,#8a7a6c 0%,#b9b3ad 40%,#e2e2e2 60%,#d94e9a 85%)}
.hero-frame{left:600px;top:100px;width:460px;height:445px;border:2px solid var(--teal);border-top:none;border-radius:0 0 230px 230px}
.avatars{left:977px;top:232px;width:158px;height:40px;background:var(--white);border-radius:20px;display:flex;align-items:center;padding-left:14px}
.avatars span{width:28px;height:28px;border-radius:50%;border:2px solid var(--white);margin-left:-6px}
.scroll{left:544px;top:653px;width:112px;height:112px;border-radius:50%;background:var(--white);box-shadow:0 6px 20px rgba(0,0,0,.08)}

.mission-bg{left:-420px;top:1257px;width:2040px;height:900px;border-radius:50% 50% 0 0/280px 280px 0 0;background:linear-gradient(180deg,var(--mist) 0%,var(--pink) 30%,#fdf4f5 65%,var(--white) 100%)}
.divider{left:93px;top:2043px;width:1012px;height:1px;background:#c9c9c9}

.card{position:absolute;top:2642px;width:190px;height:234px;background:var(--white);border-radius:14px;box-shadow:0 2px 10px rgba(0,0,0,.1)}
.card .pic{position:absolute;left:26px;top:22px;width:138px;height:192px;border-radius:4px;border:4px solid #6fd9de}

.footer-bg{left:-500px;top:3834px;width:2200px;height:700px;border-radius:50% 50% 0 0/230px 230px 0 0;background:var(--ink)}
.cta{left:205px;top:3658px;width:789px;height:194px;border-radius:97px;background:var(--teal)}
.fbtn{position:absolute;top:4003px;height:41px;border-radius:22px;font-size:10.5px;font-weight:500;display:flex;align-items:center;justify-content:center;color:var(--ink)}
</style>
</head>
<body>

<!-- Hero -->
<div class="abs hero-bg"></div>
<header class="abs nav">
  <div class="abs brand" style="left:36px;top:26px">
    <span class="brand-dot"></span>Hollow Birch
  </div>
  <div class="abs menu">
    <svg width="58" height="58" viewBox="0 0 58 58"><g stroke="#fff" stroke-width="2.4" stroke-linecap="round"><line x1="20" y1="22" x2="38" y2="22"/><line x1="20" y1="29" x2="38" y2="29"/><line x1="24" y1="36" x2="38" y2="36"/></g></svg>
  </div>
</header>

<svg class="spark" style="left:52px;top:186px" viewBox="0 0 40 34"><g stroke="var(--teal)" stroke-width="4" stroke-linecap="round"><line x1="4" y1="18" x2="30" y2="28"/><line x1="10" y1="8" x2="30" y2="22"/><line x1="24" y1="2" x2="32" y2="16"/></g></svg>
<h1 class="abs display" style="left:95px;top:214px;font-size:34px;line-height:1.45">Bringing<br>comfort, joy and<br>unconditional</h1>
<p class="abs display" style="left:95px;top:376px;font-size:19px">Love one paw at a time.</p>
<p class="abs copy" style="left:95px;top:412px;color:var(--ink);white-space:nowrap">A Michigan Nonprofit dedicated to providing Therapy Dogs to the community to spread joy.</p>
<a class="btn" style="left:95px;top:443px;width:158px;height:39px">Click Here to Donate</a>

<div class="photo hero-photo" role="img" aria-label="Husky therapy dog wearing a pink flowered bandana"></div>
<div class="abs hero-frame"></div>
<div class="abs avatars" role="img" aria-label="Volunteer profile pictures">
  <span style="background:#e9e4dc;margin-left:0"></span><span style="background:#e39a7a"></span><span style="background:#c98a6a"></span><span style="background:#9b8d5c"></span><span style="background:#f26a3a;display:flex;align-items:center;justify-content:center;font-size:8px;color:#fff">+4</span>
</div>

<div class="abs scroll">
  <svg width="112" height="112" viewBox="0 0 112 112">
    <defs><path id="ringpath" d="M56,56 m-38,0 a38,38 0 1,1 76,0 a38,38 0 1,1 -76,0"/></defs>
    <text font-family="Outfit,sans-serif" font-size="9" letter-spacing="3.2" fill="#111"><textPath href="#ringpath">SCROLL DOWN • SCROLL DOWN •</textPath></text>
    <circle cx="56" cy="56" r="24" fill="var(--teal)"/>
    <g stroke="#fff" stroke-width="2.4" fill="none" stroke-linecap="round"><line x1="56" y1="45" x2="56" y2="66"/><polyline points="48,58 56,66 64,58"/></g>
  </svg>
</div>

<!-- Our story -->
<div class="photo ring" style="left:189px;top:804px;width:376px;height:376px;background:linear-gradient(150deg,#c9c2b6 0%,#8b7b6c 45%,#3b3a3c 100%)" role="img" aria-label="Three therapy dogs sitting together in vests and bandanas"></div>
<div class="photo" style="left:440px;top:1036px;width:145px;height:145px;border-radius:50%;border:4px solid var(--white);background:linear-gradient(150deg,#e46a2c 0%,#6b5a4e 50%,#2b2b2b 100%)" role="img" aria-label="Close-up of a fluffy therapy dog"></div>
<svg class="spark" style="left:606px;top:860px" viewBox="0 0 40 34"><g stroke="var(--teal)" stroke-width="4" stroke-linecap="round"><line x1="4" y1="18" x2="30" y2="28"/><line x1="10" y1="8" x2="30" y2="22"/><line x1="24" y1="2" x2="32" y2="16"/></g></svg>
<h2 class="abs display section-title" style="left:649px;top:886px">Our story</h2>
<div class="abs copy" style="left:649px;top:928px;width:370px">
  <p>Every wag tells a story – and ours began with a simple belief: the love of a dog can change lives.</p>
  <p style="margin-top:12px">What started with a few volunteers and their dogs has grown into a community dedicated to bringing comfort and joy wherever it's needed most. From hospitals to schools and senior centers, our therapy dog teams share moments of connection, calm, and healing – one visit at a time.</p>
  <p style="margin-top:12px">At the heart of our mission is a simple truth – sometimes the best kind of therapy comes with four paws and a wagging tail.</p>
</div>
<a class="btn" style="left:649px;top:1094px;width:134px;height:42px">Request a Visit</a>

<!-- Our mission -->
<div class="abs mission-bg"></div>
<svg class="spark" style="left:452px;top:1390px" viewBox="0 0 40 34"><g stroke="var(--teal)" stroke-width="4" stroke-linecap="round"><line x1="4" y1="18" x2="30" y2="28"/><line x1="10" y1="8" x2="30" y2="22"/><line x1="24" y1="2" x2="32" y2="16"/></g></svg>
<h2 class="abs display section-title" style="left:494px;top:1415px">Our mission</h2>
<p class="abs copy" style="left:300px;top:1458px;width:600px;text-align:center">To certify, and deploy therapy dog teams that promote emotional well-being, reduce stress, and foster empathy. We are dedicated to improving quality of life by bringing the unconditional love and calming presence of therapy dogs to those in need, while upholding the highest standards of animal welfare, professionalism, and community service</p>
<div class="photo" style="left:164px;top:1535px;width:872px;height:406px;border-radius:30px;background:linear-gradient(180deg,#6a7a4a 0%,#c69a5e 35%,#8a5a34 60%,#3d5a2a 100%)" role="img" aria-label="Seven smiling dogs sitting in a row on a lawn, video preview"></div>
<div class="abs" style="left:550px;top:1891px;width:100px;height:100px;border-radius:50%;background:var(--teal)">
  <svg width="100" height="100" viewBox="0 0 100 100"><polygon points="43,38 64,50 43,62" fill="#111"/></svg>
</div>
<div class="abs divider"></div>

<!-- Our purpose -->
<svg class="spark" style="left:154px;top:2190px" viewBox="0 0 40 34"><g stroke="var(--teal)" stroke-width="4" stroke-linecap="round"><line x1="4" y1="18" x2="30" y2="28"/><line x1="10" y1="8" x2="30" y2="22"/><line x1="24" y1="2" x2="32" y2="16"/></g></svg>
<h2 class="abs display section-title" style="left:197px;top:2218px">Our purpose</h2>
<div class="abs copy" style="left:197px;top:2260px;width:370px">
  <p>Our purpose is to share the comfort, joy, and healing power of the human animal bond. We connect trained therapy dog teams with people in need of emotional support, companionship, and encouragement in hospitals, schools, senior communities, and beyond.</p>
  <p style="margin-top:12px">Through every visit, we aim to lift spirits, ease stress, and remind people that kindness and connection can come on four paws and a wagging tail.</p>
</div>
<a class="btn" style="left:197px;top:2388px;width:146px;height:38px">Click Here to Join</a>
<div class="photo ring" style="left:669px;top:2108px;width:376px;height:376px;background:linear-gradient(160deg,#7a8a9a 0%,#d89a5a 40%,#c47a3a 70%,#6a4a3a 100%)" role="img" aria-label="Smiling red therapy dog in a harness"></div>
<div class="photo" style="left:643px;top:2337px;width:150px;height:150px;border-radius:50%;border:4px solid var(--white);background:linear-gradient(150deg,#2a3a6a 0%,#8a3a4a 50%,#3a3a3a 100%)" role="img" aria-label="Therapy dog resting on a colorful blanket"></div>

<!-- Team -->
<svg class="spark" style="left:420px;top:2555px" viewBox="0 0 40 34"><g stroke="var(--teal)" stroke-width="4" stroke-linecap="round"><line x1="4" y1="18" x2="30" y2="28"/><line x1="10" y1="8" x2="30" y2="22"/><line x1="24" y1="2" x2="32" y2="16"/></g></svg>
<h2 class="abs display section-title" style="left:462px;top:2583px">What our team</h2>
<div class="card" style="left:98px"><div class="pic" role="img" aria-label="Team card for Luna, husky in pink bandana" style="background:linear-gradient(180deg,#8fd6f2 0%,#d9d4cc 45%,#e06aa8 100%)"></div></div>
<div class="card" style="left:302px"><div class="pic" role="img" aria-label="Team card for Koa, shepherd dog" style="background:linear-gradient(180deg,#7fb8e8 0%,#3a3430 50%,#6aa0d8 100%)"></div></div>
<div class="card" style="left:505px"><div class="pic" role="img" aria-label="Team card for Stoick, golden retriever" style="background:linear-gradient(180deg,#8fd6f2 0%,#d8a050 50%,#7a5a3a 100%)"></div></div>
<div class="card" style="left:708px"><div class="pic" role="img" aria-label="Team card for Elliott, dog lying on a dock" style="background:linear-gradient(180deg,#9ad0f0 0%,#5a3a2a 50%,#4a6aa0 100%)"></div></div>
<div class="card" style="left:911px"><div class="pic" role="img" aria-label="Team card for Sky, husky in pink bandana" style="background:linear-gradient(180deg,#8fd6f2 0%,#d9d4cc 45%,#e06aa8 100%)"></div></div>

<!-- Donors -->
<svg class="spark" style="left:392px;top:2950px" viewBox="0 0 40 34"><g stroke="var(--teal)" stroke-width="4" stroke-linecap="round"><line x1="4" y1="18" x2="30" y2="28"/><line x1="10" y1="8" x2="30" y2="22"/><line x1="24" y1="2" x2="32" y2="16"/></g></svg>
<h2 class="abs display section-title" style="left:435px;top:2978px">Donors referrals</h2>
<div class="abs copy" style="left:260px;top:3024px;width:680px;text-align:center">
  <p>Our donors and referral partners are the heart of our organization. Because of their generosity, we are able to keep costs low for our therapy dog teams while never compromising the integrity, training, and care of our handlers and dogs.</p>
  <p style="margin-top:12px">Every visit, every wagging tail, and every moment of comfort is made possible by your kindness, our dedicated volunteers, and a whole lot of furry friends and helping paws.</p>
  <p style="margin-top:12px;color:var(--ink);font-weight:600">Thank you for believing in our mission and helping us spread healing one paw at a time.</p>
</div>

<div class="photo ring" style="left:189px;top:3174px;width:376px;height:376px;background:linear-gradient(160deg,#b08a6a 0%,#c8703a 40%,#2a2a2a 65%,#8a6a4a 100%)" role="img" aria-label="Three dogs stacked playfully in an autumn field"></div>
<h2 class="abs display section-title" style="left:619px;top:3240px">Corporate donors</h2>
<p class="abs display" style="left:619px;top:3287px;font-size:16px">BrightLine</p>
<p class="abs copy" style="left:619px;top:3316px;white-space:nowrap">Cloud Phone Systems Build for Reliable Business Communications.</p>
<p class="abs display" style="left:619px;top:3344px;font-size:16px;line-height:1.25">Cedar Hollow Post 12 of the<br>Veterans League</p>
<p class="abs copy" style="left:619px;top:3398px;width:400px">Serving Veterans from the local community since 1930. To all who have served America: THANK YOU!</p>
<a class="btn" style="left:619px;top:3444px;width:133px;height:39px">Request a Visit</a>

<div class="abs" style="left:68px;top:3340px;width:48px;height:48px;border-radius:50%;background:var(--ink)">
  <svg width="48" height="48" viewBox="0 0 48 48"><g stroke="#fff" stroke-width="2.4" fill="none" stroke-linecap="round"><line x1="33" y1="24" x2="15" y2="24"/><polyline points="22,17 15,24 22,31"/></g></svg>
</div>
<div class="abs" style="left:1081px;top:3340px;width:48px;height:48px;border-radius:50%;background:var(--teal)">
  <svg width="48" height="48" viewBox="0 0 48 48"><g stroke="#fff" stroke-width="2.4" fill="none" stroke-linecap="round"><line x1="15" y1="24" x2="33" y2="24"/><polyline points="26,17 33,24 26,31"/></g></svg>
</div>

<!-- Contact + footer -->
<div class="abs footer-bg"></div>
<a class="abs cta">
  <span class="abs display" style="left:90px;top:50px;font-size:38px;line-height:1.2">Please click here<br>to contact us</span>
</a>

<div class="abs brand" style="left:97px;top:3970px;font-size:44px;color:var(--white);gap:14px">
  <span class="brand-dot" style="width:40px;height:40px;background:var(--white)"></span>Hollow Birch
</div>
<a class="fbtn" style="left:602px;width:171px;background:var(--teal)">Click here to Join!</a>
<a class="fbtn" style="left:781px;width:169px;background:var(--white)">Click Here To Donate!</a>
<a class="fbtn" style="left:958px;width:147px;background:var(--teal)">Request a Visit!</a>
<div class="abs" style="left:93px;top:4105px;width:1012px;height:1px;background:#3a3a3a"></div>
<p class="abs" style="left:0;top:4118px;width:1200px;text-align:center;font-size:9.5px;color:var(--white)">© 2026 Hollow Birch. All Rights Reserved.</p>

</body>
</html>
```